Wireless Broadband Newspaper AD

We have recently re-branded our company, new logo and website.

Our primary product offering is Wireless Broadband services to region, the target audience generally cannot get ADSL broadband.

We wanted to pose the question "Can't get ADSL ?" to attract the attention of those who are unable to access conventional mass market broadband offerings.

Ad Size should be:
129mm Wide
178mm High

Please find the text for the AD below.

Can't get ADSL ?
Try Fixed Wireless Broadband

* Speeds up to 10Mbit
* Plans from $29.95 per month
* Up to 60GB Download Allowance
* $99 Professional On-site Installation
* No Contracts

http://talvonet.com.au
CALL NOW - 1300 47 91 36

-

Target Market(s)

Frequent Internet users, requiring broadband access in their homes.

Industry/Entity Type

It Company

Requirements
Must have
• Ensure that the general branding feel of the existing website is considered, please us similar colours and theme.
• As well as our logo, which you will find attached in EPS format.
• http://talvonet.com.au
Nice to have
• Large caption "Can't get ADSL?"

```html
<!DOCTYPE html>
<html lang="en">
<head>
<meta charset="utf-8">
<title>Talvonet – Can't get ADSL?</title>
<link rel="stylesheet" href="https://fonts.googleapis.com/css2?family=Audiowide&family=Exo+2:wght@500;600&display=swap">
<style>
  :root {
    --bg-light: #6a6a6a;
    --bg-mid: #4a4a4a;
    --bg-dark: #262626;
    --orange: #f7931e;
    --white: #ffffff;
    --photo-cool: #6f8494;
    --photo-cool-dark: #4d5a63;
    --device-light: #e6e8ea;
    --device-mid: #aeb3b8;
    --device-dark: #7b8086;
  }
  html, body {
    margin: 0;
    padding: 0;
    overflow: hidden;
    background: var(--bg-dark);
  }
  .ad {
    position: relative;
    width: 1200px;
    height: 900px;
    overflow: hidden;
    background: radial-gradient(ellipse at 55% 40%, var(--bg-light) 0%, var(--bg-mid) 45%, var(--bg-dark) 100%);
    font-family: "Exo 2", sans-serif;
    color: var(--white);
  }
  .headline {
    position: absolute;
    top: 28px;
    left: 0;
    width: 1200px;
    margin: 0;
    text-align: center;
    font-family: "Audiowide", sans-serif;
    font-weight: 400;
    font-size: 98px;
    line-height: 1.2;
    color: var(--orange);
    text-shadow: 4px 4px 6px rgba(0,0,0,0.7);
  }
  .headline .mark { color: var(--white); }
  .globe-art {
    position: absolute;
    left: 1030px;
    top: 150px;
    width: 160px;
    height: 220px;
    border-radius: 10px;
    background: linear-gradient(160deg, var(--photo-cool) 0%, var(--photo-cool-dark) 100%);
    opacity: 0.6;
  }
  .cable-art {
    position: absolute;
    left: 600px;
    top: 550px;
    width: 130px;
    height: 130px;
    border-radius: 16px;
    background: linear-gradient(160deg, var(--photo-cool), var(--photo-cool-dark));
    opacity: 0.55;
  }
  .router-box-art {
    position: absolute;
    left: 960px;
    top: 400px;
    width: 230px;
    height: 210px;
    border-radius: 4px;
    background: linear-gradient(180deg, #f4f5f6 0%, var(--device-mid) 100%);
  }
  .router-art {
    position: absolute;
    left: 860px;
    top: 625px;
    width: 330px;
    height: 260px;
    border-radius: 26px 26px 10px 10px;
    background: linear-gradient(170deg, var(--device-light) 0%, var(--device-mid) 70%, var(--device-dark) 100%);
  }
  .subhead {
    position: absolute;
    top: 198px;
    left: 0;
    width: 1200px;
    margin: 0;
    text-align: center;
    font-weight: 600;
    font-size: 52px;
    line-height: 1.2;
    letter-spacing: 3px;
    text-shadow: 2px 2px 4px rgba(0,0,0,0.6);
  }
  .features {
    position: absolute;
    top: 282px;
    left: 44px;
    margin: 0;
    padding: 0;
    list-style: none;
    font-weight: 500;
    font-size: 46px;
    line-height: 57px;
    letter-spacing: 2.5px;
    text-shadow: 2px 2px 4px rgba(0,0,0,0.6);
  }
  .features li::before {
    content: "* ";
    color: var(--orange);
  }
  .features .hl { color: var(--orange); }
  .brand {
    position: absolute;
    left: 200px;
    top: 625px;
    display: flex;
    align-items: center;
    gap: 16px;
  }
  .brand-dot {
    width: 70px;
    height: 70px;
    border-radius: 50%;
    background: var(--orange);
  }
  .brand-name {
    font-weight: 600;
    font-size: 66px;
    color: var(--orange);
  }
  .call {
    position: absolute;
    top: 768px;
    left: 12px;
    margin: 0;
    font-family: "Audiowide", sans-serif;
    font-size: 52px;
    line-height: 1.2;
    color: var(--orange);
    text-shadow: 3px 3px 5px rgba(0,0,0,0.7);
    white-space: nowrap;
  }
  .call .number { color: var(--white); }
  .web {
    position: absolute;
    top: 846px;
    left: 44px;
    margin: 0;
    font-weight: 500;
    font-size: 40px;
    line-height: 1.2;
    letter-spacing: 4px;
    text-shadow: 2px 2px 4px rgba(0,0,0,0.6);
  }
</style>
</head>
<body>
<main class="ad">
  <div class="globe-art" role="img" aria-label="Photo of a glowing globe of the earth"></div>
  <div class="cable-art" role="img" aria-label="Photo of an ethernet cable plug"></div>
  <div class="router-box-art" role="img" aria-label="Photo of a wireless router retail box"></div>
  <div class="router-art" role="img" aria-label="Photo of a white wireless router"></div>

  <h1 class="headline">Can't get ADSL<span class="mark">?</span></h1>
  <p class="subhead">Try Fixed Wireless Broadband</p>

  <ul class="features">
    <li>Speeds up to <span class="hl">10Mbit</span></li>
    <li>Plans from <span class="hl">$29.95</span> per month</li>
    <li>Up to <span class="hl">60GB</span> Download Allowance</li>
    <li><span class="hl">$99</span> Professional On-site Installation</li>
    <li>No Contracts</li>
  </ul>

  <div class="brand">
    <span class="brand-dot"></span>
    <span class="brand-name">talvonet</span>
  </div>

  <p class="call">CALL NOW - <span class="number">1300 47 91 36</span></p>
  <p class="web">http://talvonet.com.au</p>
</main>
</body>
</html>
```